Indoor Gun Range Web Design Project

Create a professional bold indoor gun range website. Logo colors are white, red, and black. This is a very professional gun range. Please use high quality stock images if possible. Stay away from a lot of militia type photos. Use your best judgement on what to put as a main image and headline.

Here are some websites that I like for design.

http://www.harborlinefirearms.example/
http://www.pagecrafthub.example/website-templates/51947.html
http://www.brightmarkworks.example/

Target Market(s)

Men ages 25-65

Industry/Entity Type

Gun

Requirements
Must have
• Bold lettering, logo attached, exciting photos.
Should not have
• A lot of militia photos.

```html
<!DOCTYPE html>
<html lang="en">
<head>
<meta charset="utf-8">
<title>True Mark Indoor Gun Range</title>
<link href="https://fonts.googleapis.com/css2?family=Archivo+Black&family=Arimo:wght@400;700&display=swap" rel="stylesheet">
<style>
:root{
  --red:#d3141c;
  --red-dark:#a10d12;
  --red-light:#e52a2f;
  --ink:#1c1c1c;
  --paper:#f4f4f4;
  --slate:#3b3f44;
  --slate-dark:#2c2f33;
  --footer:#1f2023;
  --footer-line:#33353a;
  --muted:#8a8d92;
  --yellow:#f6c21c;
  --yellow-dark:#e09a0c;
}
*{box-sizing:border-box;margin:0;padding:0}
html,body{width:980px;height:1200px;overflow:hidden}
body{font-family:"Arimo",Arial,sans-serif;color:var(--ink);background:var(--paper);position:relative}

.topnav{position:absolute;left:0;top:0;width:980px;height:42px;background:linear-gradient(#e2262c,#b70f15);border-bottom:2px solid #7e0a0e}
.topnav ul{list-style:none;display:flex;position:absolute;left:98px;top:0;height:42px;align-items:center}
.topnav li{color:#fff;font-weight:700;font-size:14px;margin-right:24px;letter-spacing:.2px}
.topnav li.current{color:#ffd7d7}
.account{position:absolute;right:80px;top:14px;display:flex;gap:26px;font-size:11px;color:#fff}

.header{position:absolute;left:0;top:44px;width:980px;height:102px;background:linear-gradient(#fafafa,#eeeeee)}
.brand{position:absolute;left:96px;top:31px;display:flex;align-items:center;gap:12px}
.brand-name{font-weight:700;font-size:21px;color:var(--red);line-height:1.05;letter-spacing:.3px}
.brand-mark{width:26px;height:26px;border-radius:50%;background:var(--ink)}
.social{position:absolute;right:96px;top:36px;display:flex;gap:6px}
.social span{width:36px;height:36px;border-radius:50%;background:#2a2a2a;display:block}

.hero{position:absolute;left:97px;top:146px;width:785px;height:347px;background:linear-gradient(100deg,#3a332e 0%,#8b7b69 30%,#b9a184 55%,#8c7d6c 80%,#6f655b 100%)}
.hero-arrow{position:absolute;top:296px}
.hero-copy{position:absolute;left:352px;top:178px;width:420px;color:#fff}
.hero-title{font-family:"Archivo Black",Arial,sans-serif;font-size:34px;line-height:1;color:#111;letter-spacing:.5px}
.hero-title em{font-style:normal;color:var(--red);font-size:40px}
.hero-text{margin-top:8px;font-size:14px;line-height:17px;text-shadow:0 1px 2px rgba(0,0,0,.6)}
.join{margin-top:14px;display:inline-block;padding:9px 20px;border-radius:4px;background:linear-gradient(var(--yellow),var(--yellow-dark));font-weight:700;font-size:17px;color:#2a1d00;border:1px solid #b77c05}

.features{position:absolute;left:0;top:497px;width:980px;height:385px;background:radial-gradient(ellipse at 50% 40%,#4a4e54 0%,var(--slate) 45%,var(--slate-dark) 100%);border-top:2px dotted #6a6d72}
.card{position:absolute;top:34px;width:186px;height:306px;background:#fff;overflow:hidden}
.card-head{height:42px;display:flex;align-items:center;padding-left:12px;gap:8px;font-weight:700;font-size:15px;border-bottom:4px solid var(--red)}
.card-photo{width:186px}
.ticks{list-style:none;padding:10px 10px 0 12px}
.ticks li{display:flex;gap:6px;font-size:9px;line-height:11px;color:#444;margin-bottom:9px}
.more{display:inline-flex;align-items:center;gap:5px;padding:3px 6px 3px 11px;border-radius:10px;background:#e4e4e4;font-size:9px;color:#333;border:1px solid #cfcfcf}
.more i{width:10px;height:10px;border-radius:50%;background:var(--red);display:inline-block;position:relative}
.more i::after{content:"";position:absolute;left:3px;top:2px;border-left:5px solid #fff;border-top:3px solid transparent;border-bottom:3px solid transparent}
.overlay{position:absolute;left:0;top:179px;width:166px;padding:10px 12px;background:rgba(20,20,20,.72);color:#fff;font-size:11px;line-height:13px}
.review{padding:12px 16px 0;font-size:9px;line-height:11px;color:#444}
.review b{display:block;margin-top:8px;color:#333}
.news{list-style:none}
.news li{display:flex;gap:8px;padding:10px 8px 8px 0;border-bottom:1px solid #e3e3e3;height:62px}
.date{width:28px;flex:none;text-align:center}
.date b{display:block;background:#3a3d42;color:#fff;font-size:13px;padding:3px 0}
.date span{font-size:8px;color:#999}
.news h4{font-size:10px;line-height:12px;color:#222}
.news p{font-size:8.5px;line-height:10px;color:#555}

.footer{position:absolute;left:0;top:882px;width:980px;height:318px;background:var(--footer)}
.f-title{display:flex;align-items:center;gap:8px;color:var(--red-light);font-size:13px}
.links{position:absolute;left:97px;top:40px}
.link-cols{display:flex;gap:0;margin-top:12px}
.link-cols ul{list-style:none;width:156px}
.link-cols li{font-size:9px;color:#8e9196;line-height:14px;padding-left:12px;position:relative}
.link-cols li::before{content:"";position:absolute;left:2px;top:5px;width:4px;height:4px;border-radius:50%;background:#7a7d82}
.link-cols li.gap{margin-top:8px}
.link-cols li.hot{color:var(--red-light)}
.mail{position:absolute;left:425px;top:40px;width:200px}
.mail p{font-size:9px;color:#b3b5b9;margin-top:14px}
.mail .field{margin-top:8px;width:190px;height:18px;background:#fff;border-radius:2px}
.mail .go{margin-top:8px;display:inline-block;font-size:9px;color:var(--red);background:#f2dede;border-radius:9px;padding:3px 9px}
.share{margin-top:14px;width:190px;height:30px;background:#fff;border-radius:3px;display:flex;align-items:center;gap:6px;padding:0 8px;font-size:9px;color:#555}
.share span.b{width:42px;height:14px;background:#dde6ee;border:1px solid #b9c8d6;border-radius:2px}
.share span.c{padding:1px 5px;border:1px solid #ccc;border-radius:2px}
.ghost-brand{position:absolute;left:672px;top:52px;display:flex;align-items:center;gap:10px;color:#3a3c41;font-weight:700;font-size:14px;line-height:1.1}
.ghost-brand i{width:50px;height:50px;border-radius:50%;border:2px solid #3a3c41;display:block}
.copyright{position:absolute;left:97px;top:232px;font-size:9px;line-height:13px;color:#8a8d92}
.powered{position:absolute;left:739px;top:232px;padding:4px 10px;border-radius:9px;background:#2c2e32;font-size:9px;color:#8a8d92}
.f-rule{position:absolute;left:0;top:213px;width:980px;height:1px;background:var(--footer-line)}
</style>
</head>
<body>

<nav class="topnav">
  <ul>
    <li>HOME</li><li>RANGE FEES</li><li class="current">RANGE RULES</li><li>RANGE NEWS</li><li>MEMBERSHIP</li><li>CONTACT</li>
  </ul>
  <div class="account"><span>Sign In &#9679;</span><span>Sign Up &#9679;</span></div>
</nav>

<header class="header">
  <div class="brand">
    <div class="brand-name">TRUE MARK<br>INDOOR GUN RANGE</div>
    <span class="brand-mark"></span>
  </div>
  <div class="social"><span></span><span></span></div>
</header>

<svg class="hero-arrow" style="left:64px" width="22" height="40" viewBox="0 0 22 40"><path d="M19 2 3 20l16 18" fill="none" stroke="#c9c9c9" stroke-width="3"/></svg>
<svg class="hero-arrow" style="left:894px" width="22" height="40" viewBox="0 0 22 40"><path d="M3 2l16 18L3 38" fill="none" stroke="#c9c9c9" stroke-width="3"/></svg>

<section class="hero" role="img" aria-label="Shooters in ear protection firing handguns on an outdoor range">
  <div class="hero-copy">
    <div class="hero-title">INDOOR<em>GUN</em>RANGE!</div>
    <p class="hero-text">Lorem ipsum dolor sit amet, consectetur adipiscing elit.<br>Praesent &nbsp;elementum dui id. Consectetur adipiscing sed non est eu lectus adipiscing hendrerit.</p>
    <span class="join">Join Membership!</span>
  </div>
</section>

<section class="features">
  <article class="card" style="left:97px">
    <div class="card-head">
      <svg width="12" height="12" viewBox="0 0 12 12"><path d="M1 11l1-3 6-6 2 2-6 6z" fill="#222"/></svg>Featured Rules
    </div>
    <div class="card-photo" role="img" aria-label="Man holding a handgun in front of a city building" style="height:150px;background:linear-gradient(#8c969e,#5d6268 60%,#3f4246)"></div>
    <ul class="ticks">
      <li><svg width="12" height="10" viewBox="0 0 12 10"><path d="M1 5l3.5 3.5L11 1" fill="none" stroke="#6fa52b" stroke-width="2.2"/></svg>Lorem ipsum dolor sit amet, conse ctetur adipis cing elit.</li>
      <li><svg width="12" height="10" viewBox="0 0 12 10"><path d="M1 5l3.5 3.5L11 1" fill="none" stroke="#6fa52b" stroke-width="2.2"/></svg>Lorem ipsum dolor sit amet, conse ctetur adipis cing elit.</li>
    </ul>
    <div style="padding-left:28px"><span class="more">Learn More <i></i></span></div>
  </article>

  <article class="card" style="left:297px">
    <div class="card-head">
      <svg width="12" height="12" viewBox="0 0 12 12"><rect x="1" y="1" width="10" height="10" fill="none" stroke="#222" stroke-width="1.5"/><path d="M3 6l2 2 4-4" fill="none" stroke="#222" stroke-width="1.5"/></svg>What's Speciality?
    </div>
    <div class="card-photo" role="img" aria-label="Man in a suit holding a pistol" style="height:260px;background:linear-gradient(#aeb3b8,#6b7075 55%,#2e3033)"></div>
    <p class="overlay">Mauris pretium metus eu arcu aliquet sit amet vulput ate eros suscipit.</p>
    <div style="position:absolute;left:14px;top:276px"><span class="more">Learn More <i></i></span></div>
  </article>

  <article class="card" style="left:496px">
    <div class="card-head">
      <svg width="13" height="12" viewBox="0 0 13 12"><path d="M1 2h8v5H4l-3 3z" fill="#222"/><path d="M10 4h2v6l-2-2H6V8" fill="#222"/></svg>Recent Reviews
    </div>
    <div class="card-photo" role="img" aria-label="Man aiming a handgun at close range" style="height:116px;background:linear-gradient(#d9d4cf,#8f8078 60%,#4a3f3a)"></div>
    <p class="review">Lorem ipsum dolor sit amet, conse ctetur adipis cing elit.Lorem ipsum dolor sit amet, conse ctetur adipis cing elit.Lorem ipsum dolor sit amet, conse ctetur adipis cing elit.<b>Martin Hale, UAE</b></p>
    <div style="padding:12px 0 0 18px"><span class="more">Learn More <i></i></span></div>
  </article>

  <article class="card" style="left:696px">
    <div class="card-head">
      <svg width="12" height="11" viewBox="0 0 12 11"><path d="M0 1h2M4 1h8M0 5.5h2M4 5.5h8M0 10h2M4 10h8" stroke="#222" stroke-width="2"/></svg>News Range
    </div>
    <ul class="news">
      <li><div class="date"><b>12</b><span>Jan</span></div><div><h4>Lorem ipsum dolor sit ame</h4><p>Vivamus felis augue, facilisis nec, tristique sed nulla.</p></div></li>
      <li><div class="date"><b>11</b><span>Jan</span></div><div><h4>Lorem ipsum dolor sit ame</h4><p>Vivamus felis augue, facilisis nec, tristique sed nulla.</p></div></li>
      <li style="height:88px;border:none"><div class="date"><b>10</b><span>Jan</span></div><div><h4>Lorem ipsum dolor sit ame</h4><p>Lorem ipsum dolor sit amet, conse ctetur adipis cing elit.Lorem ipsum dolor sit amet, conse ctetur adipis cing</p></div></li>
    </ul>
    <div style="padding:0 0 0 34px"><span class="more">Learn More <i></i></span></div>
  </article>
</section>

<footer class="footer">
  <div class="links">
    <div class="f-title">
      <svg width="13" height="9" viewBox="0 0 13 9"><ellipse cx="6.5" cy="4.5" rx="6" ry="4" fill="#e52a2f"/><circle cx="6.5" cy="4.5" r="1.8" fill="#1f2023"/></svg>
      True Mark Indoor Gun Range Quick Links
    </div>
    <div class="link-cols">
      <ul>
        <li>Home</li><li>Why Us?</li><li>Contact Us</li><li>FAQ</li>
        <li class="gap">Live Chat</li><li>Testimonials</li><li>Our Corporate Reviews</li><li>New batch for the Month</li>
      </ul>
      <ul>
        <li>Range Fees</li><li>Range Rules</li><li>Range Support</li><li>Locate us</li>
        <li class="gap">Membership</li><li class="hot">Range Corporate Class</li><li>Collaboration &amp; Awards</li><li>News</li>
      </ul>
    </div>
  </div>

  <div class="mail">
    <div class="f-title">
      <svg width="12" height="12" viewBox="0 0 12 12"><circle cx="6" cy="6" r="6" fill="#e52a2f"/><path d="M3 6h6M6 3l3 3-3 3" fill="none" stroke="#1f2023" stroke-width="1.5"/></svg>
      Join Our Mail Listing
    </div>
    <p>Please enter you email address to subscribe</p>
    <div class="field"></div>
    <span class="go">Subscribe</span>
    <div class="share"><span class="b"></span><span class="c">1,186</span><span class="b" style="width:34px"></span><span class="c">19</span></div>
  </div>

  <div class="ghost-brand">TRUE MARK<br>INDOOR GUN RANGE<i></i></div>

  <div class="f-rule"></div>
  <p class="copyright">Copyright - 2012. All right reserved.<br>All brand and product names are trademarks or registered trademarks of their respective companies.</p>
  <span class="powered">Powered By : Northpine Studio</span>
</footer>

</body>
</html>
```